Promotional Advertisement and Promotional Flyer

I am a Finance Broking business (refer to my website www.harlowlending.com.au). I am sponsoring a local Crossfit Competition (Iron Clash 4) in South Australia. The idea behind this is to get some Home Loan (or even business lending) customers from the sponsorship.
I need to have 2 designs as follows:

- 1 A5 sized advertisement to go in the event program. This is to promote my business and seek customers.
- The second design is an A5 sized flyer that can be handed out to people, again promoting my business.

I would like to include my logo and also my personal photo on the flyer. I only want to include the logo and writing in the program advertisement.

Target Market(s)

Target audience is people attending a local Crossfit event. Most of these people are potential home loan customers, but may also be potential business customers.

I am looking for a professional looking advertisement.

Industry/Entity Type

Business

Requirements
Must have
• - Must have my logo
- Flyer must have my photo - not too large or dominating though. Maximum of a quarter of the page.
- Contact Details:
Phone 1300 457 216
Fax: 1300 457 284
Email: enquiries@harlowlending.com.au
Address:
Brenton Court, East Foyer
7/238 Calloway Street
ADELAIDE SA 5000

Both to include the following:

Harlow Lending is a Finance Broking business with extensive experience in the wider finance industry. We can provide expert advice and a high level of service to customers for Home Loans, Business Loans and Commercial Property Loans. Owner, Trent Harlow, has over a decade of experience working in the banking industry, covering lending channels from retail banking (branch network) through to large scale Corporate and Commercial banking. He now uses the experience and knowledge gained during his banking career to the benefit of his clients when sourcing and negotiating them the best Home Loan or Business Loan. For further information please refer to the website www.harlowlending.com.au or contact Trent Harlow on 1300 457 216.
Nice to have
• You can work with one or more of the attached promo photos also.

```html
<!DOCTYPE html>
<html lang="en">
<head>
<meta charset="utf-8">
<title>Harlow Lending – Program Advertisement and Flyer</title>
<link href="https://fonts.googleapis.com/css2?family=Source+Sans+3:wght@400;600&family=PT+Sans+Narrow&display=swap" rel="stylesheet">
<style>
  :root {
    --stage: #dcdcdc;
    --paper: #ffffff;
    --ink: #231f20;
    --tan: #c9a766;
    --rule: #6d6d6d;
    --office-light: #e9ecef;
    --office-dark: #5a6068;
    --sunset-glow: #f0a030;
    --sunset-mid: #c2461a;
    --sunset-dark: #2a1208;
    --portrait-light: #bfa98a;
    --portrait-dark: #3e3a36;
  }
  * { box-sizing: border-box; margin: 0; padding: 0; }
  html, body { width: 1200px; height: 900px; overflow: hidden; }
  body {
    position: relative;
    background: var(--stage);
    font-family: "Source Sans 3", "Helvetica Neue", Arial, sans-serif;
    color: var(--ink);
  }
  .piece { position: absolute; background: var(--paper); overflow: hidden; box-shadow: 0 2px 6px rgba(0,0,0,.18); }
  .abs { position: absolute; }

  .brand-name { font-family: "Source Sans 3", Arial, sans-serif; font-weight: 600; color: var(--ink); line-height: 1; white-space: nowrap; }
  .brand-mark { display: inline-block; background: var(--tan); border-radius: 50%; }

  .contact { text-align: right; line-height: 1.3; }
  .contact .gap { margin-top: 1.1em; }
  .divider { background: var(--rule); width: 1px; }
  .rule { background: var(--ink); height: 2px; }

  .photo-office { background: linear-gradient(100deg, var(--office-light) 0%, #b8bec6 45%, var(--office-dark) 100%); }
  .photo-sunset { background: radial-gradient(circle at 62% 40%, var(--sunset-glow) 0%, var(--sunset-mid) 30%, var(--sunset-dark) 100%); }
  .photo-portrait { background: linear-gradient(160deg, var(--portrait-light) 0%, #7d6f60 50%, var(--portrait-dark) 100%); }

  .about { font-family: "PT Sans Narrow", "Arial Narrow", sans-serif; text-align: justify; line-height: 1.35; }

  /* Program advertisement */
  .ad { left: 26px; top: 374px; width: 610px; height: 428px; }
  .ad .logo { left: 34px; top: 78px; display: flex; align-items: center; gap: 12px; }
  .ad .logo .brand-name { font-size: 34px; }
  .ad .logo .brand-mark { width: 18px; height: 18px; }
  .ad .divider { left: 307px; top: 36px; height: 142px; }
  .ad .contact { right: 19px; top: 10px; font-size: 10.5px; }
  .ad .apply { right: 19px; top: 124px; font-size: 23px; }
  .ad .web { right: 19px; top: 156px; font-size: 17px; }
  .ad .rule { left: 0; top: 203px; width: 610px; }
  .ad .photo-a { left: 0; top: 209px; width: 303px; height: 114px; }
  .ad .photo-b { left: 308px; top: 209px; width: 302px; height: 114px; }
  .ad .band { left: 0; top: 331px; width: 610px; height: 97px; background: var(--tan); padding: 6px 19px; }
  .ad .about { font-size: 10.2px; }

  /* Flyer */
  .flyer { left: 670px; top: 95px; width: 500px; height: 708px; }
  .flyer .logo { left: 46px; top: 68px; display: flex; align-items: center; gap: 10px; }
  .flyer .logo .brand-name { font-size: 26px; }
  .flyer .logo .brand-mark { width: 14px; height: 14px; }
  .flyer .divider { left: 251px; top: 30px; height: 108px; }
  .flyer .contact { right: 21px; top: 35px; font-size: 11.5px; }
  .flyer .rule { left: 0; top: 152px; width: 500px; }
  .flyer .photo-a { left: 0; top: 159px; width: 250px; height: 101px; }
  .flyer .photo-b { left: 256px; top: 159px; width: 244px; height: 101px; }
  .flyer .tagline { left: 0; top: 265px; width: 500px; height: 45px; background: var(--ink); color: var(--paper); font-size: 15.5px; line-height: 1.3; text-align: center; padding-top: 3px; }
  .flyer .photo-portrait { left: 0; top: 314px; width: 250px; height: 218px; }
  .flyer .services { left: 256px; top: 314px; width: 244px; height: 218px; background: var(--tan); padding: 8px 16px 0 22px; }
  .services h2 { font-weight: 400; font-size: 15.5px; line-height: 1.2; }
  .services p { font-family: "PT Sans Narrow", "Arial Narrow", sans-serif; font-size: 10px; line-height: 1.45; padding-left: 12px; margin: 2px 0 8px; }
  .flyer .body-copy { left: 20px; top: 537px; width: 460px; font-size: 10px; }
  .flyer .cta { left: 0; top: 636px; width: 500px; height: 56px; background: var(--ink); color: var(--paper); text-align: center; padding-top: 3px; }
  .cta .apply { font-size: 25px; line-height: 1.1; }
  .cta .web { font-size: 18px; line-height: 1.1; }
</style>
</head>
<body>

<section class="piece ad" aria-label="Program advertisement">
  <div class="abs logo"><span class="brand-name">Harlow Lending</span><span class="brand-mark"></span></div>
  <div class="abs divider"></div>
  <address class="abs contact" style="font-style:normal">
    <div>Phone: 1300 457 216</div>
    <div>Fax: 1300 457 284</div>
    <div>Email: enquiries@harlowlending.com.au</div>
    <div class="gap">Brenton Court, East Foyer, 7/238 Calloway Street</div>
    <div>ADELAIDE SA 5000</div>
  </address>
  <div class="abs apply">Apply Now!</div>
  <div class="abs web">www.harlowlending.com.au</div>
  <div class="abs rule"></div>
  <div class="abs photo-office photo-a" role="img" aria-label="Three businessmen shaking hands in a bright office"></div>
  <div class="abs photo-sunset photo-b" role="img" aria-label="Construction crane silhouetted against an orange sunset"></div>
  <div class="abs band">
    <p class="about">Harlow Lending is a Finance Broking business with extensive experience in the wider finance industry. We can provide expert advice and a high level of service to customers for Home Loans, Business Loans and Commercial Property Loans. Owner, Trent Harlow, has over a decade of experience working in the banking industry, covering lending channels from retail banking (branch network) through to large scale Corporate and Commercial banking. He now uses the experience and knowledge gained during his banking career to the benefit of his clients when sourcing and negotiating them the best Home Loan or Business Loan. For further information please refer to the website www.harlowlending.com.au or contact Trent Harlow on 1300 457 216.</p>
  </div>
</section>

<section class="piece flyer" aria-label="Flyer">
  <div class="abs logo"><span class="brand-name">Harlow Lending</span><span class="brand-mark"></span></div>
  <div class="abs divider"></div>
  <address class="abs contact" style="font-style:normal">
    <div>Phone: 1300 457 216</div>
    <div>Fax: 1300 457 284</div>
    <div>Email: enquiries@harlowlending.com.au</div>
    <div class="gap">Brenton Court, East Foyer</div>
    <div>7/238 Calloway Street</div>
    <div>ADELAIDE SA 5000</div>
  </address>
  <div class="abs rule"></div>
  <div class="abs photo-office photo-a" role="img" aria-label="Three businessmen shaking hands in a bright office"></div>
  <div class="abs photo-sunset photo-b" role="img" aria-label="Construction crane silhouetted against an orange sunset"></div>
  <div class="abs tagline">A personalised approach to helping you achieve a superior outcome<br>for your personal or business finances</div>
  <div class="abs photo-portrait" role="img" aria-label="Portrait of the owner in a suit seated at a desk"></div>
  <div class="abs services">
    <h2>Commercial Property Finance</h2>
    <p>Experienced in Commercial Property Development and Investment Finance</p>
    <h2>Agribusiness</h2>
    <p>Harlow Lending has a keen understanding of farming and other Agribusiness enterprises.</p>
    <h2>Commercial Finance</h2>
    <p>Leverage off of Harlow Lending's experience, knowledge and contacts to achieve a superior outcome for your commercial finance arrangements.</p>
  </div>
  <p class="abs about body-copy">Harlow Lending is a Finance Broking business with extensive experience in the wider finance industry. We can provide expert advice and a high level of service to customers for Home Loans, Business Loans and Commercial Property Loans. Owner, Trent Harlow, has over a decade of experience working in the banking industry, covering lending channels from retail banking (branch network) through to large scale Corporate and Commercial banking. He now uses the experience and knowledge gained during his banking career to the benefit of his clients when sourcing and negotiating them the best Home Loan or Business Loan. For further information please refer to the website www.harlowlending.com.au or contact Trent Harlow on 1300 457 216.</p>
  <div class="abs cta">
    <div class="apply">Apply Now!</div>
    <div class="web">www.harlowlending.com.au</div>
  </div>
</section>

</body>
</html>
```